contemporary upscale hair salon

we need a business card design for a modern upscale salon. I would like the card to be vertical, simple, and easy to read. I would like a black matte finish on the info side with white on the back of the card, white lettering with a splash of red incorporated somewhere in there. I also want to incorporate embossing and/or cut out in the letters. The info I would like; Name of the business (Velora Salon) stylist name (Janet) phone number(4075319264) and web address (www.veloraexample.com) I am open to putting shears on the card but without it looking too cheap. Looking for something really modern and edgy. these are just ideas I have, but feel free to show me your creative ideas.
please note: the website is still under construction please do not use any images or colors off the web page. Also i currently do not have a logo, that will be a future project.

```html
<!DOCTYPE html>
<html lang="en">
<head>
<meta charset="utf-8">
<title>Velora Salon — Business Card</title>
<link rel="stylesheet" href="https://fonts.googleapis.com/css2?family=Roboto:wght@400;500&display=swap">
<style>
  :root {
    --backdrop: #e7e4e0;
    --card-dark: #3a3a3b;
    --emboss-face: #4a4a4c;
    --emboss-light: rgba(255, 255, 255, 0.12);
    --emboss-dark: rgba(0, 0, 0, 0.45);
    --card-light: #cbcac6;
    --accent: #a8155a;
    --card-shadow: rgba(0, 0, 0, 0.28);
  }
  * { box-sizing: border-box; margin: 0; padding: 0; }
  html, body {
    width: 1200px;
    height: 900px;
    overflow: hidden;
    background: var(--backdrop);
    font-family: "Roboto", Arial, sans-serif;
  }
  .stage {
    position: relative;
    width: 1200px;
    height: 900px;
  }
  .card {
    position: absolute;
    top: 225px;
    width: 300px;
    height: 450px;
    box-shadow: 0 6px 16px var(--card-shadow);
  }
  .card--front {
    left: 270px;
    background: var(--card-dark);
  }
  .card--back {
    left: 630px;
    background: var(--card-light);
  }
  .shears-emboss {
    position: absolute;
    left: 62px;
    top: 100px;
    width: 190px;
    height: 205px;
    border-radius: 6px;
    background: linear-gradient(150deg, var(--emboss-face), #424244);
    box-shadow:
      inset 2px 2px 0 var(--emboss-light),
      inset -2px -2px 0 var(--emboss-dark),
      1px 2px 4px var(--emboss-dark);
  }
  .wordmark {
    color: var(--accent);
    font-weight: 500;
    font-size: 25px;
    line-height: 1.2;
  }
  .card--front .wordmark {
    position: absolute;
    right: 26px;
    bottom: 38px;
    text-align: right;
  }
  .card--back .wordmark {
    position: absolute;
    left: 110px;
    top: 135px;
    text-align: left;
  }
  .card--back .wordmark .line-2 {
    padding-left: 10px;
  }
  .stylist-name {
    position: absolute;
    right: 30px;
    bottom: 110px;
    color: var(--accent);
    font-size: 26px;
    font-weight: 500;
  }
  .contact {
    position: absolute;
    right: 30px;
    bottom: 42px;
    color: var(--accent);
    font-size: 12px;
    line-height: 1.5;
    text-align: right;
    letter-spacing: 0.3px;
  }
</style>
</head>
<body>
  <main class="stage">
    <section class="card card--front" aria-label="Card front">
      <div class="shears-emboss" role="img" aria-label="Embossed outline of hair-cutting shears"></div>
      <p class="wordmark">Velora<br>Salon</p>
    </section>

    <section class="card card--back" aria-label="Card back">
      <p class="wordmark"><span class="line-1">Velora</span><br><span class="line-2">Salon</span></p>
      <p class="stylist-name">Janet</p>
      <p class="contact">407 531 9264<br>www.veloraexample.com</p>
    </section>
  </main>
</body>
</html>
```